Online-Marketing Material für Schlüsseldienst
Zielgruppe
Wir bieten einen Schlüsseldienst mit Montagen im Bereich Sicherheitstechnik sowie Öffnungen jeder Art
Aufgabenstellung
Suche ein Stimmungsbild für den Kopfbereich unter der Navigation (730x160px). Design soll zur Seite passen, bitte vorhandene URL ansehen. Bild muss auch auf auf kleinem Viewport mobile funktionieren. Die Farben sollen entsprechend passen. Es könnte auch eine Collage sein, ähnlich wie aktuell von mir selbst gemacht(kesselwerk-tuerhilfe.example), natürlich nicht so stupide. Bitte Seite mit dem Browser verkleinern um das Bild auf seine Funktionalität zu überprüfen. Thema der Collage/des Stimmungsbildes im Kopfbereich könnten Montagen, Schlüssel, Schlüssel, Einbruchschutz, Autoschlüssel, Türöffnungen, Tresoröffnungen, Notdienst oder ähnliches sein.
Außerdem brauche ich entsprechend zu dem Stimmungsbild noch ein Nexora Local Profil Cover Photo in der Größe 1024 x 576 pixels (16:9 aspect ratio). Dies soll als Titelbild für mein Local Business dienen.

```html
<!DOCTYPE html>
<html lang="de">
<head>
<meta charset="utf-8">
<title>Kesselwerk Türhilfe Frankfurt am Main</title>
<link href="https://fonts.googleapis.com/css2?family=Roboto:wght@400;700&display=swap" rel="stylesheet">
<style>
  :root {
    --teal: #2c6763;
    --teal-dark: #275c59;
    --red: #c1271d;
    --page: #efefef;
    --white: #ffffff;
    --rule: #d8d8d8;
    --link: #0a1ee6;
  }
  * { margin: 0; padding: 0; box-sizing: border-box; }
  html, body { width: 1200px; height: 992px; overflow: hidden; }
  body { background: var(--page); font-family: "Roboto", Arial, sans-serif; color: var(--teal); position: relative; }
  .page { position: absolute; left: 65px; top: 0; width: 1059px; height: 992px; background: var(--white); border-left: 1px solid #ddd; border-right: 1px solid #ddd; }
  .nav { position: absolute; left: 0; top: 0; width: 100%; height: 54px; background: var(--teal); display: flex; gap: 0; }
  .nav a { position: absolute; top: 0; line-height: 52px; color: var(--white); text-decoration: none; font-size: 22px; }
  .hero { position: absolute; left: 0; top: 54px; width: 100%; height: 232px; background: linear-gradient(90deg, #8a7a6a 0%, #c9b39a 22%, #6d665e 42%, #3a3634 58%, #7c6d60 75%, #b9c2c8 100%); }
  .hero-band { position: absolute; left: 2px; right: 5px; bottom: 0; height: 16px; background: var(--teal-dark); opacity: .9; }
  .abs { position: absolute; white-space: nowrap; }
  .title { font-size: 40px; font-weight: 700; letter-spacing: 1.2px; line-height: 48px; }
  .title.red { color: var(--red); }
  .lead { font-size: 21px; letter-spacing: .5px; line-height: 28px; }
  .alert { font-size: 21px; font-weight: 700; color: var(--red); letter-spacing: .4px; line-height: 28px; }
  .phone { font-size: 35px; font-weight: 700; letter-spacing: 1.5px; line-height: 42px; }
  .rule { position: absolute; height: 1px; background: var(--rule); }
  .sub { font-size: 22px; font-weight: 700; line-height: 28px; }
  .divider { position: absolute; left: 740px; top: 327px; width: 1px; height: 665px; background: var(--rule); }
  .side { position: absolute; left: 740px; width: 319px; text-align: center; font-size: 21px; line-height: 28px; }
  .side a { color: var(--link); font-size: 20px; }
  .side .strong { font-weight: 700; }
  .side .tel { font-weight: 700; letter-spacing: 3px; }
  .service-art { position: absolute; left: 783px; top: 402px; width: 232px; height: 195px; background: radial-gradient(ellipse at 60% 45%, #d8e8c8 0%, #eef0ee 45%, #f6f6f6 75%); }
  .cert { position: absolute; left: 823px; top: 805px; width: 154px; height: 187px; background: #b9bcbf; }
  .cert-band { position: absolute; left: 0; bottom: 0; width: 100%; height: 26px; background: #2f5a7a; }
</style>
</head>
<body>
<div class="page">
  <nav class="nav">
    <a style="left:79px">Schlüsseldienst</a>
    <a style="left:289px">Schließanlagen</a>
    <a style="left:499px">Autoöffnung</a>
    <a style="left:673px">Autoschlüssel</a>
    <a style="left:866px">Impressum</a>
  </nav>
  <div class="hero" role="img" aria-label="Collage: Autoschlüssel an Autotür, Schlüsselbund, Montage eines Schlosses mit Akkuschrauber, Tresorschloss, Schlüsselübergabe an Kunden">
    <div class="hero-band"></div>
  </div>

  <div class="abs title red" style="left:74px;top:329px">Kesselwerk Türhilfe</div>
  <div class="abs title" style="left:74px;top:386px">Frankfurt am Main</div>
  <div class="abs lead" style="left:74px;top:461px">Die Tür ist zugefallen, Sie haben sich ausgesperrt? Ist</div>
  <div class="abs lead" style="left:74px;top:499px">der Schlüssel abgebrochen oder stecken geblieben?</div>
  <div class="abs alert" style="left:74px;top:564px">Über 10.000 bestätigte Türöffnungen!</div>
  <div class="abs lead" style="left:74px;top:629px">Rufen Sie uns an, wir helfen gerne.</div>
  <div class="abs phone" style="left:74px;top:675px">☎ 069 - 555 010 42</div>
  <div class="abs alert" style="left:74px;top:743px">Unsere Öffnungs-Preise sind inkl. Anfahrt,</div>
  <div class="abs alert" style="left:74px;top:781px">Rechnung mit MwSt. sowie Abend- oder</div>
  <div class="abs alert" style="left:74px;top:820px">Nachtzuschlag - keine weiteren Kosten!</div>
  <div class="rule" style="left:77px;top:883px;width:602px"></div>
  <div class="abs sub" style="left:77px;top:900px">Öffnungs-Preise für zugezogene Türen:</div>
  <div class="rule" style="left:77px;top:942px;width:602px"></div>
  <div class="abs sub" style="left:77px;top:959px">Montag - Freitag</div>

  <div class="divider"></div>
  <div class="side" style="top:342px"><a href="#">Locksmith Frankfurt</a></div>
  <div class="service-art" role="img" aria-label="Telefonhörer mit 24-Stunden-Symbol"></div>
  <div class="side strong" style="top:620px">Kesselwerk Türhilfe</div>
  <div class="side" style="top:653px">Frankfurt am Main</div>
  <div class="side" style="top:685px">Hessen</div>
  <div class="side tel" style="top:717px">069 / 555 010 42</div>
  <div class="rule" style="left:740px;top:762px;width:319px"></div>
  <div class="cert" role="img" aria-label="Zertifizierungssiegel"><div class="cert-band"></div></div>
</div>
</body>
</html>
```